Amber Hollow Productions

I need a business card design for a new freelance film production company using or incorporating the logo:
I want the card to be creative, minimal, yet professional. Feel free to use a variety of different shapes and sizes/ textures for the card.

Industry/Entity Type

Film Production

```html
<!DOCTYPE html>
<html lang="en">
<head>
<meta charset="utf-8">
<title>Amber Hollow Productions — Business Cards</title>
<link rel="stylesheet" href="https://fonts.googleapis.com/css2?family=Tenor+Sans&family=Open+Sans:wght@400&display=swap">
<style>
  :root {
    --page: #ffffff;
    --card-grey: #c1c1c4;
    --card-grey-light: #cbcbce;
    --brand-blue: #2b5ba9;
    --band-purple: #5d3f92;
    --band-purple-deep: #3f2a72;
    --text-white: #f4f4f6;
  }
  * { margin: 0; padding: 0; box-sizing: border-box; }
  html, body {
    width: 1200px; height: 899px; overflow: hidden;
    background: var(--page);
  }
  .canvas { position: relative; width: 1200px; height: 899px; }

  .card {
    position: absolute;
    background: linear-gradient(160deg, var(--card-grey-light), var(--card-grey));
    overflow: hidden;
  }

  /* Back face: wordmark */
  .card--back { left: 400px; top: 434px; width: 720px; height: 386px; }
  .wordmark {
    position: absolute; left: 0; right: 0; top: 122px;
    text-align: center;
    font-family: "Tenor Sans", sans-serif;
    color: var(--brand-blue);
  }
  .wordmark__name {
    display: block;
    font-size: 68px; line-height: 1; letter-spacing: 0.02em;
  }
  .wordmark__line {
    display: block; margin-top: 20px;
    font-size: 22px; letter-spacing: 0.95em; padding-left: 0.95em;
  }

  /* Front face: contact side */
  .card--front { left: 51px; top: 86px; width: 698px; height: 400px; z-index: 2; }
  .card__band { position: absolute; left: 0; top: 0; width: 698px; height: 400px; }
  .front-name {
    position: absolute; left: 40px; top: 205px;
    font-family: "Tenor Sans", sans-serif;
    font-size: 30px; letter-spacing: 0.03em;
    color: var(--brand-blue);
  }
  .info {
    position: absolute;
    font-family: "Open Sans", sans-serif;
    font-size: 30px;
    color: var(--text-white);
  }
  .info--upper { left: 349px; top: 122px; }
  .info--band { left: 349px; top: 264px; }
</style>
</head>
<body>
<main class="canvas">
  <section class="card card--back" aria-label="Card back">
    <h1 class="wordmark">
      <span class="wordmark__name">AMBER HOLLOW</span>
      <span class="wordmark__line">PRODUCTIONS</span>
    </h1>
  </section>

  <section class="card card--front" aria-label="Card front">
    <svg class="card__band" viewBox="0 0 698 400" aria-hidden="true">
      <defs>
        <linearGradient id="bandFill" x1="0" y1="0" x2="0" y2="1">
          <stop offset="0" stop-color="#6b4da0"/>
          <stop offset="0.45" stop-color="#5d3f92"/>
          <stop offset="1" stop-color="#3f2a72"/>
        </linearGradient>
      </defs>
      <path d="M0 306 L300 306 C318 306 318 251 345 251 L640 251 C668 251 668 272 698 272 L698 400 L0 400 Z"
            fill="url(#bandFill)"/>
    </svg>
    <p class="front-name">AMBER HOLLOW</p>
    <p class="info info--upper">information</p>
    <p class="info info--band">information</p>
  </section>
</main>
</body>
</html>
```